Accounting business needs business card

I have a business card but need something better. I want the colour changed and the design to be better. I have uploaded a picture of my new sign that is grey in colour, i would like to incorporate these colours.

```html
<!DOCTYPE html>
<html lang="en">
<head>
<meta charset="utf-8">
<title>Northvale Tax – Business Card</title>
<link href="https://fonts.googleapis.com/css2?family=Montserrat:wght@400;500;800&display=swap" rel="stylesheet">
<style>
  :root{
    --stage:#2b2b2b;
    --card-black:#1d1d1f;
    --pattern-black:#232325;
    --silver-light:#e9e9ea;
    --silver-mid:#c4c4c6;
    --ink:#1a1a1a;
    --blue:#2c8fd1;
    --blue-bright:#29abe2;
    --badge-blue:#0d5aa7;
    --white:#ffffff;
    --soft-white:#d8d8d8;
  }
  *{margin:0;padding:0;box-sizing:border-box}
  html,body{width:1200px;height:900px;overflow:hidden;background:var(--stage)}
  body{font-family:"Montserrat",sans-serif;position:relative}

  .card{position:absolute;width:640px;height:366px;border-radius:14px;overflow:hidden;box-shadow:0 14px 30px rgba(0,0,0,.45)}

  /* back of card */
  .card-back{left:60px;top:56px;background:var(--card-black)}
  .card-back .pattern-field{position:absolute;inset:0;background:radial-gradient(circle at 40% 40%,#2a2a2d 0%,var(--pattern-black) 70%)}
  .card-back .back-mark{position:absolute;right:60px;top:58px;display:flex;align-items:center;gap:10px;color:var(--blue-bright);font-weight:500;font-size:16px;letter-spacing:3px}
  .back-mark .mark-circle{width:40px;height:40px;border:2px solid var(--blue-bright);border-radius:50%}

  /* front of card */
  .card-front{left:500px;top:470px;background:linear-gradient(135deg,var(--silver-light) 0%,var(--silver-mid) 100%)}
  .card-front .swoosh{position:absolute;inset:0}
  .holder{position:absolute;left:38px;top:112px;width:290px;color:var(--ink)}
  .holder-name{font-weight:800;font-size:29px;line-height:1}
  .holder-credentials{font-size:12.5px;margin-top:8px;color:#333}
  .holder-title{font-size:13.5px;margin-top:3px;color:#333;padding-bottom:10px;border-bottom:1.5px solid var(--ink)}
  .contact-list{list-style:none;margin-top:12px}
  .contact-list li{display:flex;align-items:center;gap:12px;font-size:15px;margin-bottom:7px}
  .contact-list svg{width:14px;height:14px;flex:none;fill:var(--ink)}

  .brand{position:absolute;right:40px;top:60px;width:230px;text-align:center;color:var(--white)}
  .brand-circle{width:92px;height:92px;border:3px solid var(--soft-white);border-radius:50%;margin:0 auto 20px}
  .brand-name{font-weight:500;font-size:26px;letter-spacing:12px;color:var(--soft-white)}
  .brand-sub{font-weight:500;font-size:11px;letter-spacing:5px;color:var(--soft-white);margin-top:6px}

  .credentials{position:absolute;right:26px;bottom:36px;display:flex;align-items:center;gap:10px}
  .badge-member{width:88px;height:30px;background:linear-gradient(90deg,var(--badge-blue) 60%,#f2c400 60%)}
  .credential-note{font-size:9.5px;line-height:1.25;color:var(--white);width:100px}
  .badge-partner{position:absolute;right:26px;top:232px;width:40px;height:40px;border-radius:50%;background:var(--blue-bright)}
</style>
</head>
<body>

<section class="card card-back" aria-label="Card back">
  <div class="pattern-field" role="img" aria-label="Repeating monogram pattern in dark grey across the card back"></div>
  <div class="back-mark"><span class="mark-circle"></span>NORTHVALE</div>
</section>

<section class="card card-front" aria-label="Card front">
  <svg class="swoosh" viewBox="0 0 640 366" preserveAspectRatio="none" aria-hidden="true">
    <path d="M262 0 C205 150 290 330 520 366 L640 366 L640 0 Z" fill="var(--blue)"/>
    <path d="M286 0 C236 150 320 318 540 366 L640 366 L640 0 Z" fill="#111"/>
    <path d="M296 0 C250 150 330 312 560 366 L640 366 L640 0 Z" fill="var(--card-black)"/>
  </svg>

  <div class="holder">
    <h1 class="holder-name">Liam Harwood</h1>
    <p class="holder-credentials">CPA, MTAX, BCOM ( Acc &amp; Fin )</p>
    <p class="holder-title">Taxation and Business Accountant</p>
    <ul class="contact-list">
      <li><svg viewBox="0 0 16 16"><path d="M3 1l3 3-2 2c1 2 3 4 5 5l2-2 3 3-2 3C6 15 1 10 1 3z"/></svg>0412 555 018</li>
      <li><svg viewBox="0 0 16 16"><path d="M1 3h14v10H1z M1 3l7 6 7-6" stroke="#e6e6e6" stroke-width="1"/></svg>liam@northvaletax.com.au</li>
      <li><svg viewBox="0 0 16 16"><circle cx="8" cy="8" r="7"/></svg>www.northvaletax.com.au</li>
    </ul>
  </div>

  <div class="brand">
    <div class="brand-circle"></div>
    <div class="brand-name">NORTHVALE</div>
    <div class="brand-sub">TAX</div>
  </div>

  <div class="badge-partner" role="img" aria-label="Software partner badge"></div>
  <div class="credentials">
    <div class="badge-member" role="img" aria-label="Professional body membership badge"></div>
    <p class="credential-note">Northvale is a Certified Business</p>
  </div>
</section>

</body>
</html>
```